Web Design Project

I work in a sign company that print banners, back light films, and vinyl lettering. We also create metal store signs that lights up. We have a laser cutter that can cut plastics and a waterjet that can cut stainless steel.
Job: Create a homepage
Requirements:
1. Keep it simple and neat, I do not want it to be messy. (Similar to this website, plover, or this http://www.markelvo.example/)
2. A navigation bar that has (Will help if you show a template for one of these links):
-Home
-Signs
-Banners
-Lettering
-Prints
-Gallery
3.Bottom of the page
-Abous us
-Shipping and Returning Policy
-Resellers
4.Other (Somewhere easy to find)
-Login
-Shopping Cart
-Upload
Updates
Nice job designers. I am currently working on the Site's logo, so I will be posting that up later.
I would like you guys to change the selection on the navigation bar.
It should only have:
Banners
Lettering
Prints
Gallery
Keep up the good work
Sorry for the bad update, the Navigation bar should have:
Home
Signs
Banners
Lettering
Prints
Gallery

```html
<!DOCTYPE html>
<html lang="en">
<head>
<meta charset="utf-8">
<title>Sign Company Homepage</title>
<link href="https://fonts.googleapis.com/css2?family=Nunito:wght@800;900&family=Open+Sans:wght@400;600;700&display=swap" rel="stylesheet">
<style>
  :root {
    --brand-red: #d2232a;
    --link-red: #d9262c;
    --text-dark: #111111;
    --text-mid: #555555;
    --text-soft: #7a7a7a;
    --rule: #dcdcdc;
    --frame: #c9c9c9;
    --button-top: #f4f4f4;
    --button-bottom: #d9d9d9;
    --page-bg: #ffffff;
  }
  * { box-sizing: border-box; margin: 0; padding: 0; }
  html, body { width: 1200px; height: 900px; overflow: hidden; background: var(--page-bg); }
  body { font-family: "Open Sans", sans-serif; color: var(--text-mid); }
  .page { position: relative; width: 1200px; height: 900px; }
  .abs { position: absolute; }

  /* Header */
  .logo { left: 125px; top: 36px; font-family: "Nunito", sans-serif; font-weight: 900; font-size: 45px; color: var(--brand-red); letter-spacing: 0.5px; }
  .util-btn { top: 14px; height: 29px; border: 1px solid #bdbdbd; border-radius: 2px; background: linear-gradient(var(--button-top), var(--button-bottom)); display: flex; align-items: center; gap: 6px; padding-left: 8px; font-size: 16px; font-weight: 600; color: #3a3a3a; }
  .util-btn.upload { left: 867px; width: 101px; }
  .util-btn.login { left: 974px; width: 99px; padding-left: 10px; }
  .cart { left: 933px; top: 54px; display: flex; align-items: center; gap: 4px; font-size: 16px; color: #666; }

  .main-nav { left: 471px; top: 89px; display: flex; font-size: 16.5px; font-weight: 600; letter-spacing: 0.6px; color: #555; }
  .main-nav a { color: inherit; text-decoration: none; position: absolute; white-space: nowrap; }
  .main-nav a.active { color: var(--link-red); }
  .search { left: 867px; top: 88px; width: 206px; height: 27px; border: 1px solid #bbb; border-radius: 2px; display: flex; }
  .search span { flex: 1; padding: 3px 9px; font-size: 15px; color: #888; }
  .search .search-btn { width: 38px; border-left: 1px solid #bbb; background: linear-gradient(#fafafa, #e2e2e2); display: flex; align-items: center; justify-content: center; }

  .rule { left: 125px; width: 950px; height: 3px; background: var(--rule); }

  /* Hero */
  .hero-visual { left: 138px; top: 164px; width: 500px; height: 378px; border-radius: 4px;
    background: radial-gradient(ellipse at 55% 70%, #b9bcc0 0%, #d9dbde 35%, transparent 70%),
                linear-gradient(100deg, #b7d65a 0%, #8fc7e2 35%, #f2f2f2 60%, #ffffff 100%); }
  .slide-arrow { top: 315px; width: 39px; height: 39px; border-radius: 50%; background: linear-gradient(#f3f3f3, #d8d8d8); display: flex; align-items: center; justify-content: center; }
  .slide-arrow.prev { left: 102px; }
  .slide-arrow.next { left: 1053px; }
  .hero-title { left: 669px; top: 207px; width: 380px; font-size: 24.5px; line-height: 31px; color: var(--text-dark); font-weight: 400; }
  .hero-text { left: 670px; top: 296px; width: 350px; font-size: 17.5px; line-height: 23px; color: var(--text-soft); letter-spacing: 0.2px; }
  .read-more { left: 872px; top: 459px; display: flex; align-items: center; gap: 9px; font-size: 21px; color: var(--link-red); letter-spacing: 0.5px; text-decoration: none; }

  /* Services */
  .service { top: 570px; width: 228px; }
  .service .photo { width: 228px; height: 167px; border: 3px solid var(--frame); background-clip: padding-box; }
  .service .label { margin-top: 8px; text-align: center; font-size: 19px; font-weight: 600; letter-spacing: 0.6px; color: var(--text-mid); }

  /* News */
  .news-label { left: 134px; top: 800px; font-size: 19px; font-weight: 700; color: #555; letter-spacing: 0.5px; }
  .news-text { left: 216px; top: 804px; font-size: 14px; font-weight: 600; color: #888; }
  .news-date { left: 730px; top: 803px; font-size: 15px; color: #777; }
  .news-divider { left: 837px; top: 796px; width: 1px; height: 33px; background: var(--rule); }
  .social { top: 797px; width: 31px; height: 31px; border-radius: 5px; background: #9a9a9a; }

  /* Footer */
  .footer-links { left: 0; width: 1200px; top: 844px; text-align: center; font-size: 15px; color: #555; letter-spacing: 0.3px; }
  .footer-links a { color: inherit; text-decoration: none; }
  .copyright { left: 0; width: 1200px; top: 866px; text-align: center; font-size: 14px; color: #222; letter-spacing: 0.3px; }
</style>
</head>
<body>
<div class="page">

  <div class="abs logo">Logo Here</div>

  <div class="abs util-btn upload">
    <svg width="22" height="18" viewBox="0 0 22 18"><rect x="1" y="5" width="18" height="12" fill="#8a8a8a"/><rect x="1" y="3" width="8" height="3" fill="#8a8a8a"/><path d="M15 10 V2 M11 5 L15 1 L19 5" stroke="#555" stroke-width="2" fill="none"/></svg>
    Upload
  </div>
  <div class="abs util-btn login">
    <svg width="14" height="18" viewBox="0 0 14 18"><path d="M3 8 V5 a4 4 0 0 1 8 0 V8" stroke="#555" stroke-width="2" fill="none"/><rect x="1" y="8" width="12" height="9" rx="1" fill="#555"/></svg>
    Login
  </div>
  <div class="abs cart">
    <svg width="22" height="20" viewBox="0 0 22 20"><path d="M1 2 H4 L7 13 H18 L20 5 H5" stroke="#777" stroke-width="1.6" fill="none"/><path d="M8 8 H19 M7 10 H18" stroke="#999" stroke-width="1"/><circle cx="8" cy="17" r="1.7" fill="#777"/><circle cx="17" cy="17" r="1.7" fill="#777"/></svg>
    Shopping Cart
  </div>

  <nav class="abs main-nav">
    <a class="active" style="left:0">Banners</a>
    <a style="left:106px">Lettering</a>
    <a style="left:224px">Prints</a>
    <a style="left:311px">Gallery</a>
  </nav>
  <div class="abs search">
    <span>Search</span>
    <div class="search-btn"><svg width="20" height="20" viewBox="0 0 20 20"><circle cx="8" cy="8" r="5.5" stroke="#444" stroke-width="2" fill="none"/><path d="M12 12 L18 18" stroke="#444" stroke-width="3"/></svg></div>
  </div>

  <div class="abs rule" style="top:125px"></div>

  <section>
    <div class="abs hero-visual" role="img" aria-label="Product showcase: a roll-up banner stand, printed brochures and a pickup truck with vinyl door graphics"></div>
    <div class="abs slide-arrow prev"><svg width="14" height="18" viewBox="0 0 14 18"><path d="M10 2 L3 9 L10 16" stroke="#fff" stroke-width="3" fill="none"/></svg></div>
    <div class="abs slide-arrow next"><svg width="14" height="18" viewBox="0 0 14 18"><path d="M4 2 L11 9 L4 16" stroke="#fff" stroke-width="3" fill="none"/></svg></div>
    <h1 class="abs hero-title">Lorem ipsum dolor sit amet, consectetur adipiscing elit.</h1>
    <p class="abs hero-text">Lorem ipsum dolor sit amet, consect adipiscing elit. Suspendisse consequ semper luctus. In iaculis eros sit ame felis pulvinar dignissim. In gravida sa pien eu velit tincidunt.</p>
    <a class="abs read-more">
      <svg width="23" height="23" viewBox="0 0 23 23"><circle cx="11.5" cy="11.5" r="11.5" fill="#111"/><path d="M9 6.5 L14 11.5 L9 16.5" stroke="#fff" stroke-width="2.6" fill="none"/></svg>
      Read more
    </a>
  </section>

  <div class="abs rule" style="top:547px"></div>

  <section>
    <div class="abs service" style="left:127px">
      <div class="photo" role="img" aria-label="Photo of a large illuminated outdoor billboard sign on a building" style="background:linear-gradient(160deg,#2a2522 0%,#4b3f36 50%,#8c5a40 100%)"></div>
      <div class="label">Sign Solutions</div>
    </div>
    <div class="abs service" style="left:367px">
      <div class="photo" role="img" aria-label="Photo of a wide-format printer producing a colourful banner" style="background:linear-gradient(150deg,#c9c6cc 0%,#b98fb4 40%,#7f8fc4 70%,#e7dfe8 100%)"></div>
      <div class="label">Banners</div>
    </div>
    <div class="abs service" style="left:606px">
      <div class="photo" role="img" aria-label="Photo of an installer applying vinyl lettering to a white van" style="background:linear-gradient(150deg,#f2f2f2 0%,#e8e4e4 45%,#6c6e78 75%,#d8d8da 100%)"></div>
      <div class="label">Lettering</div>
    </div>
    <div class="abs service" style="left:845px">
      <div class="photo" role="img" aria-label="Photo of a backlit metal store sign glowing blue at night" style="background:radial-gradient(ellipse at 50% 50%,#4d6fa8 0%,#1d2433 55%,#121212 100%)"></div>
      <div class="label">Metal Store Signs</div>
    </div>
  </section>

  <div class="abs rule" style="top:791px;height:2px"></div>
  <div class="abs news-label">News :</div>
  <div class="abs news-text">Lorem ipsum dolor sit amet, consectetur adipiscing elit.</div>
  <div class="abs news-date">12, Jan 2012</div>
  <div class="abs news-divider"></div>
  <div class="abs social" style="left:987px" role="img" aria-label="Social network link"></div>
  <div class="abs social" style="left:1029px" role="img" aria-label="Video channel link"></div>
  <div class="abs rule" style="top:832px;height:2px"></div>

  <footer>
    <div class="abs footer-links"><a>About Us</a> | <a>Shipping and Returning Policy</a> | <a>Resellers</a> | <a>Terms &amp; Conditions</a></div>
    <div class="abs copyright">©Copyright 2011 Company Name, Inc.</div>
  </footer>

</div>
</body>
</html>
```